Need a fresh corporate identity for an existing Home Shopping Business in Thailand

We are one of the most active TV home shopping companies in Thailand. We need a fresh looking CI for our corporate, the colours of our corporate are Orange and Grey. We want our customers to see us as professional customer service who help them with their purchases.
The logo can be shown as a whole logo or either half logo but not less than half the logo.
Industry/Entity Type
Shopping
Requirements
Must have
- The logo should be shown at least half the logo or full logo.
Should not have
- The logo should not be shown less than half the logo.

```html
<!DOCTYPE html>
<html lang="en">
<head>
<meta charset="utf-8">
<title>Tanvoria Stationery</title>
<link href="https://fonts.googleapis.com/css2?family=Open+Sans:wght@400;600;700&display=swap" rel="stylesheet">
<style>
:root{
  --orange:#e05f24;
  --grey:#a9aaad;
  --paper:#ffffff;
  --ink:#444548;
  --ink-soft:#6b6c70;
  --backdrop:#eeeeef;
}
*{box-sizing:border-box;margin:0;padding:0}
html,body{width:1200px;height:937px;overflow:hidden}
body{background:var(--backdrop);font-family:'Open Sans',Arial,sans-serif;color:var(--ink);position:relative}
.sheet{position:absolute;background:var(--paper);box-shadow:0 1px 3px rgba(0,0,0,.12)}
.brand-name{color:var(--orange);font-weight:600;white-space:nowrap}

/* Letterhead */
.letterhead{left:184px;top:66px;width:386px;height:546px}
.letterhead .spine{position:absolute;left:0;top:0;width:26px;height:100%;background:var(--grey)}
.letterhead .band{position:absolute;left:0;top:98px;width:26px;height:360px;background:var(--orange);clip-path:polygon(0 0,100% 6%,100% 94%,0 100%)}
.letterhead .brand-name{position:absolute;left:36px;top:104px;font-size:14px}
.contact-list{position:absolute;left:272px;top:26px;list-style:none;font-size:7px;color:var(--ink)}
.contact-list li{display:flex;align-items:center;gap:4px;height:16px}
.contact-list svg{width:11px;height:11px}
.letter-body{position:absolute;left:38px;top:140px;width:300px;font-size:5.4px;line-height:1.5;color:var(--ink-soft)}
.letter-body p{margin-bottom:7px}
.letter-body .date{margin-bottom:8px}
.letter-body strong{color:var(--ink)}
.signature{width:40px;height:18px;margin:4px 0 6px;background:linear-gradient(90deg,#d7d7d9,#bfc0c3)}
.sheet-url{position:absolute;left:0;right:0;bottom:16px;text-align:center;font-size:12px;letter-spacing:2px;color:var(--ink)}

/* Folder */
.folder{left:635px;top:40px;width:461px;height:578px}
.folder .spine{position:absolute;left:0;top:0;width:43px;height:100%;background:var(--grey)}
.folder .band{position:absolute;left:0;top:106px;width:43px;height:364px;background:var(--orange);clip-path:polygon(0 0,100% 8%,100% 92%,0 100%)}
.folder .brand-name{position:absolute;left:148px;top:352px;font-size:34px}
.folder .sheet-url{bottom:22px;font-size:14px}

/* Business cards */
.card{width:177px;height:100px;border-radius:6px;overflow:hidden}
.card-front{left:45px;top:658px}
.card-front .top-band{position:absolute;left:0;top:0;width:100%;height:12px;background:var(--orange);clip-path:polygon(0 0,100% 0,100% 100%,30% 100%)}
.card-front .side{position:absolute;right:0;top:14px;width:26px;bottom:0;background:var(--grey)}
.vertical{position:absolute;writing-mode:vertical-rl;transform:rotate(180deg);white-space:nowrap}
.card-front .brand-name{left:14px;top:40px;font-size:7px}
.card-front .person{left:34px;top:38px;font-size:5.5px;line-height:1.3;color:var(--ink)}
.card-front .contact{left:62px;top:24px;font-size:4.6px;line-height:1.6;color:var(--ink)}
.card-front .address{right:6px;top:36px;font-size:4.4px;line-height:1.5;color:#fff}
.card-back{left:45px;top:782px;height:103px;background:var(--orange)}
.card-back .top-band{position:absolute;left:0;top:0;width:100%;height:10px;background:var(--grey);clip-path:polygon(0 0,100% 0,100% 100%,40% 100%)}
.card-back .side{position:absolute;right:0;top:12px;width:26px;bottom:0;background:var(--grey)}
.card-back .brand-name{color:#fff;left:68px;top:26px;font-size:10px}
.card-back .follow{right:7px;top:30px;font-size:5px;color:#fff;display:flex;gap:3px;align-items:center}
.card-back .follow i{display:inline-block;width:5px;height:5px;border-radius:50%;background:#fff}

/* Envelopes */
.envelope-front{left:264px;top:672px;width:371px;height:208px}
.envelope-front .spine{position:absolute;left:0;top:0;width:11px;height:100%;background:var(--grey)}
.envelope-front .band{position:absolute;left:0;top:38px;width:11px;height:130px;background:var(--orange);clip-path:polygon(0 0,100% 6%,100% 94%,0 100%)}
.envelope-front .brand-name{position:absolute;left:27px;top:102px;font-size:11px}
.envelope-front .sheet-url{left:120px;right:auto;bottom:16px;font-size:10px;letter-spacing:1.2px}
.envelope-back{left:737px;top:672px;width:431px;height:208px}
.envelope-back .flap{position:absolute;left:0;top:0;width:100%;height:71px;background:var(--orange);border-radius:0 0 34px 34px}
.envelope-back .flap-url{position:absolute;left:0;right:0;top:24px;text-align:center;color:#fff;font-size:16px;letter-spacing:2.4px}
</style>
</head>
<body>

<section class="sheet letterhead">
  <div class="spine"></div>
  <div class="band"></div>
  <div class="brand-name">Tanvoria</div>
  <ul class="contact-list">
    <li><svg viewBox="0 0 12 12"><circle cx="6" cy="6" r="5.4" fill="none" stroke="#444548" stroke-width=".9"/><rect x="4.2" y="3" width="3.6" height="6" rx=".6" fill="#444548"/></svg>555-014-7286</li>
    <li><svg viewBox="0 0 12 12"><circle cx="6" cy="6" r="5.4" fill="#444548"/><path d="M3.5 7.5h5v-1.5l-1-1.2h-3l-1 1.2z" fill="#fff"/></svg>555-019-5830</li>
    <li><svg viewBox="0 0 12 12"><circle cx="6" cy="6" r="5.4" fill="#444548"/><rect x="3.2" y="4" width="5.6" height="4" fill="#fff"/><path d="M3.2 4l2.8 2.2L8.8 4" fill="none" stroke="#444548" stroke-width=".6"/></svg>otressler@quellbrook.com</li>
    <li><svg viewBox="0 0 12 12"><circle cx="6" cy="6" r="5.4" fill="#444548"/><circle cx="6" cy="6" r="3" fill="none" stroke="#fff" stroke-width=".6"/><path d="M3 6h6M6 3v6" stroke="#fff" stroke-width=".6"/></svg>www.quellbrook.com</li>
  </ul>
  <div class="letter-body">
    <p class="date">July 2, 2012</p>
    <p><strong>Dear Client,</strong><br>ABC Building, def St., Country Name</p>
    <p>We are pleased to confirm our partnership for the coming season. Our team will prepare the full range of product showcases, scheduling and customer service support for every broadcast, and we will share updated plans with your office each week so that both teams can review progress, adjust timing and keep every order moving smoothly.</p>
    <p>Please find the attached schedule for the first month of programming along with the contact list for our support desk.</p>
    <p style="margin-top:18px">Should you have any questions about delivery, returns or payment options, our customer care staff are available every day of the week. We look forward to working closely with you and to bringing helpful, trusted products into the homes of our viewers across the country throughout the year ahead.</p>
    <p>Best Regards,</p>
    <div class="signature" role="img" aria-label="Handwritten signature"></div>
    <p><strong>Daniel Vesko</strong><br>Director<br><br>ABC Building, def St., Country Name</p>
  </div>
  <div class="sheet-url">www.quellbrook.com</div>
</section>

<section class="sheet folder">
  <div class="spine"></div>
  <div class="band"></div>
  <div class="brand-name">Tanvoria</div>
  <div class="sheet-url">www.quellbrook.com</div>
</section>

<section class="sheet card card-front">
  <div class="top-band"></div>
  <div class="side"></div>
  <div class="vertical brand-name">Tanvoria</div>
  <div class="vertical person">Owen Tressler<br>President</div>
  <div class="vertical contact">555-014-7286<br>555-019-5830<br>otressler@quellbrook.com<br>www.quellbrook.com</div>
  <div class="vertical address">88 Riverside Road,<br>Bangkok 10110</div>
</section>

<section class="sheet card card-back">
  <div class="top-band"></div>
  <div class="side"></div>
  <div class="vertical brand-name">Tanvoria</div>
  <div class="vertical follow">Follow us on <i></i><i></i><i></i><i></i></div>
</section>

<section class="sheet envelope-front">
  <div class="spine"></div>
  <div class="band"></div>
  <div class="brand-name">Tanvoria</div>
  <div class="sheet-url">www.quellbrook.com</div>
</section>

<section class="sheet envelope-back">
  <div class="flap"><div class="flap-url">www.quellbrook.com</div></div>
</section>

</body>
</html>
```